Business Card for By Marcus Hale

Looking to have a business card designed for my lifestyle and fitness company. My company offers personal training, online programming and nutrition advice based out of London, United Kingdom.

I'd like to see modern, sleek designs, focusing on black, matte black or matte grey. Design doesn't need to be overly descriptive as this will also be used as a personal business card. I've included my logo.

Please note that my company is no longer called "Fitness by Marcus Hale" but instead "By Marcus Hale", this is because of my other ventures. Therefore please don't use the "fitness by marcus hale" text.

information about my company can be found at www.bymarcushale.com

Company is also based out of Leeds (United Kingdom) & Perth (Australia) this could be reflected on the card.

Industry/Entity Type

Business

Contact Information for Business Card

Marcus Hale
+44 7382 615204
marcus@bymarcushale.com
www.bymarcushale.com

Font styles to use
Sans Serif

Requirements
Must have
• All contact details and inclusion of my logo.

```html
<!DOCTYPE html>
<html lang="en">
<head>
<meta charset="utf-8">
<title>By Marcus Hale — Business Card</title>
<link rel="stylesheet" href="https://fonts.googleapis.com/css2?family=Lato:wght@400&display=swap">
<style>
  :root {
    --page: #e6e6e4;
    --card-light: #ffffff;
    --card-dark: #231f20;
    --ink-dark: #1a1a1a;
    --ink-light: #ffffff;
  }
  * { margin: 0; padding: 0; box-sizing: border-box; }
  html, body {
    width: 1200px; height: 1000px; overflow: hidden;
    background: var(--page);
    font-family: "Lato", sans-serif;
  }
  .canvas { position: relative; width: 1200px; height: 1000px; }
  .card {
    position: absolute; left: 220px; width: 760px; height: 434px;
    box-shadow: 0 6px 18px rgba(0,0,0,0.25);
  }
  .card--front { top: 41px; background: var(--card-light); }
  .card--back { top: 525px; background: var(--card-dark); color: var(--ink-light); }

  .brand {
    position: absolute; display: flex; align-items: center; gap: 14px;
    font-weight: 400; white-space: nowrap;
  }
  .brand__dot { border-radius: 50%; flex: none; }
  .card--front .brand {
    left: 50%; top: 50%; transform: translate(-50%, -50%);
    font-size: 44px; color: var(--ink-dark);
  }
  .card--front .brand__dot { width: 26px; height: 26px; background: var(--ink-dark); }
  .card--back .brand {
    left: 500px; top: 140px; width: 184px; flex-direction: column; gap: 12px;
    font-size: 26px; color: var(--ink-light);
  }
  .card--back .brand__dot { width: 40px; height: 40px; background: var(--ink-light); }

  .holder-name {
    position: absolute; left: 40px; top: 150px;
    font-size: 40px; font-weight: 400; line-height: 1;
  }
  .divider {
    position: absolute; left: 40px; top: 210px; width: 388px; height: 2px;
    background: var(--ink-light);
  }
  .contact {
    position: absolute; left: 40px; display: flex; align-items: center; gap: 16px;
    font-size: 26px; line-height: 1;
  }
  .contact svg { width: 20px; height: 20px; fill: var(--ink-light); flex: none; }
  .contact--phone { top: 276px; }
  .contact--email { top: 318px; }
  .website {
    position: absolute; right: 40px; top: 346px; font-size: 23px; line-height: 1;
  }
  .locations {
    position: absolute; right: 38px; top: 382px; font-size: 17px; line-height: 1;
  }
</style>
</head>
<body>
<main class="canvas">
  <section class="card card--front" aria-label="Card front">
    <div class="brand"><span class="brand__dot"></span>By Marcus Hale</div>
  </section>

  <section class="card card--back" aria-label="Card back">
    <h1 class="holder-name">Marcus Hale</h1>
    <div class="divider"></div>
    <p class="contact contact--phone">
      <svg viewBox="0 0 24 24" aria-hidden="true"><path d="M6.6 10.8a15.1 15.1 0 0 0 6.6 6.6l2.2-2.2c.3-.3.7-.4 1-.2 1.1.4 2.3.6 3.6.6.6 0 1 .4 1 1V20c0 .6-.4 1-1 1A17 17 0 0 1 3 4c0-.6.4-1 1-1h3.5c.6 0 1 .4 1 1 0 1.3.2 2.5.6 3.6.1.3 0 .7-.2 1z"/></svg>
      +44 7382 615204
    </p>
    <p class="contact contact--email">
      <svg viewBox="0 0 24 24" aria-hidden="true"><path d="M2 5h20v14H2z M3.5 6.5 12 13l8.5-6.5z" fill-rule="evenodd"/></svg>
      marcus@bymarcushale.com
    </p>
    <div class="brand"><span class="brand__dot"></span>By Marcus Hale</div>
    <p class="website">www.bymarcushale.com</p>
    <p class="locations">Leeds (United Kingdom) &amp; Perth (Australia)</p>
  </section>
</main>
</body>
</html>
```